Business card for Northland's Blue Wagon.

Good day i am looking for a business card design for my business.
The name of the business is Northland's Blue Wagon. It is a van rental business that provides a driver and helper to the customer. Customer have use to van for small moves, studio or 1 bedroom, Moving furniture like couch or kitchen cabinets.
We are available evenings, weekends and holidays.
the means to contact us is by phone at 628-947-2071; By emails at Oakridge@northlandsbluewagon.net; or by social media, Facebook and Instagram.
You can see attached pictures of the van and or logo.

```html
<!DOCTYPE html>
<html lang="en">
<head>
<meta charset="utf-8">
<title>Northland's Blue Wagon – Business Card</title>
<link rel="stylesheet" href="https://fonts.googleapis.com/css2?family=Libre+Baskerville:wght@400;700&display=swap">
<style>
  :root {
    --backdrop: #353535;
    --card-white: #ffffff;
    --brand-red: #d52027;
    --ink: #111111;
    --shadow: rgba(0, 0, 0, 0.35);
  }
  * { box-sizing: border-box; margin: 0; padding: 0; }
  html, body {
    width: 1200px;
    height: 1200px;
    overflow: hidden;
    background: var(--backdrop);
  }
  body {
    position: relative;
    font-family: "Libre Baskerville", Georgia, serif;
    color: var(--ink);
  }
  .card {
    position: absolute;
    left: 217px;
    width: 766px;
    height: 460px;
    box-shadow: 0 4px 14px var(--shadow);
    overflow: hidden;
  }
  .card--front { top: 101px; background: var(--card-white); }
  .card--back  { top: 631px; background: var(--brand-red); }

  .brand-mark {
    position: absolute;
    display: flex;
    align-items: center;
    justify-content: center;
    text-align: center;
    font-weight: 700;
    line-height: 1.25;
  }
  .card--front .brand-mark {
    left: 530px; top: 54px; width: 182px; height: 173px;
    color: var(--brand-red);
    font-size: 22px;
  }
  .card--back .brand-mark {
    left: 223px; top: 76px; width: 324px; height: 308px;
    color: var(--card-white);
    font-size: 38px;
  }

  .holder-name {
    position: absolute;
    left: 56px; top: 161px;
    font-size: 29px;
    font-weight: 700;
    color: var(--brand-red);
  }
  .holder-title {
    position: absolute;
    left: 56px; top: 204px;
    font-size: 21px;
    font-weight: 700;
  }
  .divider {
    position: absolute;
    left: 51px; top: 237px;
    width: 664px; height: 2.5px;
    background: var(--brand-red);
  }
  .contact-row {
    position: absolute;
    left: 51px;
    display: flex;
    align-items: center;
    gap: 11px;
    font-size: 20.5px;
  }
  .contact-row--phone  { top: 252px; }
  .contact-row--email  { top: 294px; }
  .contact-row--social { top: 334px; }
  .icon-badge {
    width: 29px; height: 29px;
    border-radius: 50%;
    background: var(--ink);
    display: flex; align-items: center; justify-content: center;
    flex: none;
  }
  .icon-badge svg { width: 16px; height: 16px; }
  .contact-text--phone { font-size: 19.5px; letter-spacing: 0.6px; }

  .availability-band {
    position: absolute;
    left: 0; top: 377px;
    width: 100%; height: 32px;
    background: var(--brand-red);
    color: var(--card-white);
    font-size: 20px;
    display: flex; align-items: center; justify-content: center;
  }
</style>
</head>
<body>

  <section class="card card--front" aria-label="Business card front">
    <div class="brand-mark">Northland's<br>Blue Wagon</div>

    <h1 class="holder-name">Your Name</h1>
    <h2 class="holder-title">Your Title</h2>
    <div class="divider"></div>

    <div class="contact-row contact-row--phone">
      <span class="icon-badge">
        <svg viewBox="0 0 24 24" aria-hidden="true">
          <path fill="#fff" d="M6.6 10.8c1.4 2.8 3.8 5.1 6.6 6.6l2.2-2.2c.3-.3.7-.4 1-.2 1.1.4 2.3.6 3.6.6.6 0 1 .4 1 1V20c0 .6-.4 1-1 1C10.6 21 3 13.4 3 4c0-.6.4-1 1-1h3.5c.6 0 1 .4 1 1 0 1.3.2 2.5.6 3.6.1.3 0 .7-.2 1z"/>
        </svg>
      </span>
      <span class="contact-text contact-text--phone">628-947-2071</span>
    </div>

    <div class="contact-row contact-row--email">
      <span class="icon-badge">
        <svg viewBox="0 0 24 24" aria-hidden="true">
          <rect x="3" y="6" width="18" height="12" rx="1.5" fill="none" stroke="#fff" stroke-width="2"/>
          <path d="M3.5 7l8.5 6.5L20.5 7" fill="none" stroke="#fff" stroke-width="2"/>
        </svg>
      </span>
      <span class="contact-text">Oakridge@northlandsbluewagon.net</span>
    </div>

    <div class="contact-row contact-row--social">
      <span class="icon-badge" aria-hidden="true"></span>
      <span class="icon-badge" aria-hidden="true"></span>
      <span class="contact-text">@northlandsbluewagon.net</span>
    </div>

    <div class="availability-band">We are available in evenings, weekends and holidays</div>
  </section>

  <section class="card card--back" aria-label="Business card back">
    <div class="brand-mark">Northland's<br>Blue Wagon</div>
  </section>

</body>
</html>
```